Billboard design - consider what a billboard is

Design a billboard using my logo - Billboard is 6m x 3m
A Billboard is advertising for my company that is on a big sign.

Has to be clean and easy to read, and ideally highlights that we are Residential and Commercial builders.

Keep it clean and easy to read

The contact number for the board is

022 583 7092
www.harbourframeworks.co.nz
info@harbourframeworks.co.nz

Doesnt have to have all contact details if it doesnt fit

Has to catch peoples attention to contact us if they need a builder

Can you please change the sign to be all white writing, with black background ?
Updates

Please consider what a billboard is...

The design needs to be suitable for a billboard..

Target Market(s)

people driving past

Industry/Entity Type

Construction

Logo Text

Wellington Builder, website email address, contact number

Colors
0054AA
0677BA
7BADD7
CADEEF
E8F1F8

Requirements
Must have
• Easy to read
Nice to have
• easy to read, can clearly see contact details

```html
<!DOCTYPE html>
<html lang="en">
<head>
<meta charset="utf-8">
<title>Harbour Frameworks Billboard</title>
<link rel="stylesheet" href="https://fonts.googleapis.com/css2?family=Russo+One&family=Roboto:wght@400&display=swap">
<style>
  :root {
    --backdrop: #a7a8aa;
    --board-blue: #0054aa;
    --text-white: #ffffff;
    --brand-tint: #7badd7;
    --tower-light: #e8ecef;
    --tower-mid: #9aa3ab;
    --tower-dark: #2a2f36;
  }
  html, body {
    margin: 0;
    padding: 0;
    width: 1200px;
    height: 770px;
    overflow: hidden;
    background: var(--backdrop);
  }
  .billboard {
    position: absolute;
    left: 135px;
    top: 151px;
    width: 931px;
    height: 467px;
    background: var(--board-blue);
    overflow: hidden;
    box-shadow: 0 2px 6px rgba(0,0,0,0.25);
  }
  .tower-photo {
    position: absolute;
    left: 0;
    top: 129px;
    width: 371px;
    height: 338px;
    background: linear-gradient(100deg, var(--tower-light) 0%, var(--tower-mid) 45%, var(--tower-dark) 100%);
    clip-path: polygon(0 0, 22% 2%, 38% 14%, 52% 18%, 60% 32%, 70% 42%, 80% 60%, 92% 84%, 100% 100%, 0 100%);
  }
  .brand-name {
    position: absolute;
    left: 124px;
    top: 48px;
    width: 300px;
    margin: 0;
    font-family: "Russo One", sans-serif;
    font-weight: 400;
    font-size: 40px;
    line-height: 1.05;
    color: var(--brand-tint);
  }
  .headline {
    position: absolute;
    left: 437px;
    top: 36px;
    margin: 0;
    font-family: "Russo One", sans-serif;
    font-weight: 400;
    color: var(--text-white);
    text-transform: uppercase;
    line-height: 1;
  }
  .headline span { display: block; }
  .headline .lead { font-size: 54px; }
  .headline .residential { font-size: 70px; margin-top: 8px; }
  .headline .commercial { font-size: 50px; margin-top: 12px; }
  .headline .builders { font-size: 86px; margin-top: 10px; }
  .contact-list {
    position: absolute;
    left: 437px;
    top: 320px;
    margin: 0;
    padding: 0;
    list-style: none;
    font-family: "Roboto", sans-serif;
    font-size: 26px;
    color: var(--text-white);
  }
  .contact-list li {
    display: flex;
    align-items: center;
    height: 44px;
  }
  .contact-list svg {
    width: 24px;
    height: 24px;
    margin-right: 14px;
    fill: var(--text-white);
    flex: none;
  }
</style>
</head>
<body>
  <section class="billboard">
    <div class="tower-photo" role="img" aria-label="Photograph of a tall apartment tower seen from below"></div>
    <p class="brand-name">Harbour Frameworks</p>
    <h1 class="headline">
      <span class="lead">We are</span>
      <span class="residential">Residential</span>
      <span class="commercial">and Commercial</span>
      <span class="builders">Builders</span>
    </h1>
    <ul class="contact-list">
      <li>
        <svg viewBox="0 0 24 24" aria-hidden="true"><path d="M6.6 10.8a15.1 15.1 0 0 0 6.6 6.6l2.2-2.2a1 1 0 0 1 1-.25 11.4 11.4 0 0 0 3.6.57 1 1 0 0 1 1 1V20a1 1 0 0 1-1 1A17 17 0 0 1 3 4a1 1 0 0 1 1-1h3.5a1 1 0 0 1 1 1c0 1.25.2 2.45.57 3.57a1 1 0 0 1-.25 1z"/></svg>
        022 583 7092
      </li>
      <li>
        <svg viewBox="0 0 24 24" aria-hidden="true"><path d="M2 5h20v14H2z M3.5 6.5 12 13l8.5-6.5" fill="none" stroke="#fff" stroke-width="0"/><path d="M2 5h20v2l-10 7L2 7z"/><path d="M2 9l10 7 10-7v10H2z"/></svg>
        info@harbourframeworks.co.nz
      </li>
      <li>
        <svg viewBox="0 0 24 24" aria-hidden="true"><path d="M12 2a10 10 0 1 0 0 20 10 10 0 0 0 0-20zm-1 17.9A8 8 0 0 1 4.1 10.6L9 15.5v1a2 2 0 0 0 2 2zm6.9-2.5A2 2 0 0 0 16 16h-1v-3a1 1 0 0 0-1-1H8v-2h2a1 1 0 0 0 1-1V7h2a2 2 0 0 0 2-2v-.4a8 8 0 0 1 2.9 12.8z"/></svg>
        www.harbourframeworks.co.nz
      </li>
    </ul>
  </section>
</body>
</html>
```